Need Business cards

Im a new realtor and already have a logo. I would like to purchase a Business card design that catches customer's attention, its creative, and modern.

Marisol Quintero
Realtor ®
(555) 318 4027
marisolqtrhomes@brindlemail.com

Target Market(s)

investors, buyers and seller, property management

Industry/Entity Type

real estate,

Contact Information for Business Card

Marisol Quintero

Requirements
Must have
• BOTH LOGOS, WOULD LIKE TO SEE WITH DIFFERENT OPTIONS WITH EITHER PICTURE

```html
<!DOCTYPE html>
<html lang="en">
<head>
<meta charset="utf-8">
<title>Marisol Quintero – Realtor Business Card</title>
<link href="https://fonts.googleapis.com/css2?family=Arimo:wght@400;700&display=swap" rel="stylesheet">
<style>
  :root {
    --backdrop: #e4e2e1;
    --card: #fbfbfa;
    --ink: #1b1b1b;
    --gold: #c39a1f;
    --gold-light: #e2c35a;
    --photo-light: #eeeeee;
    --photo-mid: #9a9a9a;
    --photo-dark: #2c2c2c;
  }
  * { margin: 0; padding: 0; box-sizing: border-box; }
  html, body {
    width: 1200px;
    height: 1000px;
    overflow: hidden;
    background: var(--backdrop);
    font-family: "Arimo", Arial, sans-serif;
    color: var(--ink);
  }
  .stage {
    position: relative;
    width: 1200px;
    height: 1000px;
    display: flex;
    justify-content: center;
    align-items: center;
    gap: 80px;
  }
  .card {
    position: relative;
    width: 400px;
    height: 700px;
    background: var(--card);
    box-shadow: 0 10px 30px rgba(0,0,0,0.12);
    overflow: hidden;
  }

  /* Front: portrait side */
  .portrait {
    position: absolute;
    left: 30px;
    top: 40px;
    width: 340px;
    height: 560px;
    background:
      radial-gradient(ellipse 45% 40% at 50% 30%, var(--photo-mid) 0%, transparent 70%),
      linear-gradient(180deg, var(--photo-light) 0%, var(--photo-mid) 35%, var(--photo-dark) 60%, var(--photo-mid) 85%, var(--card) 100%);
    border-radius: 4px;
  }
  .brokerage {
    position: absolute;
    left: 40px;
    bottom: 48px;
    display: flex;
    align-items: center;
    gap: 10px;
    font-weight: 700;
    font-size: 26px;
    letter-spacing: 1px;
    color: var(--ink);
  }
  .brokerage-mark {
    width: 14px;
    height: 14px;
    background: var(--ink);
  }

  /* Back: contact side */
  .brand {
    position: absolute;
    left: 0;
    right: 0;
    top: 120px;
    display: flex;
    flex-direction: column;
    align-items: center;
    gap: 30px;
  }
  .brand-mark {
    width: 140px;
    height: 140px;
    background: linear-gradient(135deg, var(--gold-light) 0%, var(--gold) 55%, #a87f12 100%);
  }
  .brand-name {
    font-weight: 700;
    font-size: 30px;
    letter-spacing: 1.5px;
    color: var(--gold);
    white-space: nowrap;
  }
  .contact {
    position: absolute;
    left: 0;
    right: 0;
    bottom: 70px;
    text-align: center;
    font-size: 19px;
    line-height: 1.35;
  }
  .contact-name { font-size: 21px; }
  .contact-title {
    color: var(--gold);
    font-weight: 700;
    font-size: 15px;
    margin-bottom: 14px;
  }
</style>
</head>
<body>
  <main class="stage">
    <section class="card card-front">
      <div class="portrait" role="img" aria-label="Black and white portrait photograph of the realtor seated at a table"></div>
      <div class="brokerage">
        <span class="brokerage-mark"></span>
        <span class="brokerage-name">KEYSTRIDE REALTY</span>
      </div>
    </section>

    <section class="card card-back">
      <div class="brand">
        <span class="brand-mark"></span>
        <span class="brand-name">MARISOL QUINTERO</span>
      </div>
      <div class="contact">
        <p class="contact-name">Marisol Quintero</p>
        <p class="contact-title">Realtor ®</p>
        <p class="contact-phone">T.: (555) 318 4027</p>
        <p class="contact-email">E.: marisolqtrhomes@brindlemail.com</p>
      </div>
    </section>
  </main>
</body>
</html>
```